Top New England Restaurant Needs Website Redesign

We currently have a website, rmsbistro.com, but would like to redesign it. We are a casual upscale restaurant specializing in breakfast and lunch. We are one of the top rated restaurants in all of New England and would like our site to look like it as well. We'd love to have a blog/news section that will be updated weekly or so, as well as an email capture feature on the page.

The site will mostly be static, with lots of pictures (I'll take them and provide). The only part of the site that will get updated regularly is the blog and/or news (could be the same page).

Some restaurant websites I like are: www.corvintable.com, www.brassandoat.com,

Target Market(s)

Foodies, RM's Bistro customers,

Industry/Entity Type

Restaurant

Logo Text

RM's Bistro

Font styles to use
Sans Serif

Requirements
Must have
• Friendloop Like Box, Dinetip Box, Email capture, Blog/News, About Us page, Contact page

```html
<!DOCTYPE html>
<html lang="en">
<head>
<meta charset="utf-8">
<title>RM's Bistro</title>
<link href="https://fonts.googleapis.com/css2?family=Oswald:wght@400;500;700&family=Open+Sans:wght@400;600;700&display=swap" rel="stylesheet">
<style>
:root{
  --teal:#2db3d0;
  --teal-deep:#1d8ea8;
  --teal-dark:#17748a;
  --ink:#333;
  --muted:#666;
  --paper:#f1f1f1;
  --white:#fff;
  --night:#262626;
  --night-deep:#1b1b1b;
  --rating:#d32323;
}
*{box-sizing:border-box;margin:0;padding:0}
html,body{width:1200px;height:3550px;overflow:hidden}
body{position:relative;font-family:"Open Sans",Arial,sans-serif;color:var(--ink);background:var(--white)}
.abs{position:absolute}
.heading{font-family:"Oswald",Arial,sans-serif;font-weight:500;text-transform:uppercase;letter-spacing:.5px}
.photo{position:absolute}

/* header & hero */
.hero{left:0;top:0;width:1200px;height:640px;background:linear-gradient(120deg,#e9e2d2 0%,#c9b79a 18%,#5b3a28 40%,#3a2418 58%,#8a5a32 75%,#b9874e 100%)}
.hero-shade{left:0;top:0;width:1200px;height:640px;background:linear-gradient(90deg,rgba(0,0,0,.25),rgba(0,0,0,0) 45%)}
.logo{left:130px;top:0;width:185px;height:80px;background:var(--teal);display:flex;align-items:center;justify-content:center;color:var(--white);font-family:"Oswald",sans-serif;font-weight:700;font-size:34px;letter-spacing:.5px}
.nav{left:445px;top:28px;display:flex;gap:0;align-items:center}
.nav a{font-family:"Oswald",sans-serif;font-size:14px;color:var(--white);text-decoration:none;text-transform:uppercase;margin-right:30px;padding-bottom:4px}
.nav a.active{color:var(--teal);border-bottom:2px solid var(--teal)}
.nav-phone{left:950px;top:21px;width:118px;height:38px;border:2px solid var(--white);color:var(--white);font-family:"Oswald",sans-serif;font-size:14px;display:flex;align-items:center;justify-content:center;gap:8px}
.hero-title{left:133px;top:350px;font-size:58px;color:var(--white);font-weight:500;text-shadow:0 2px 6px rgba(0,0,0,.35)}
.hero-btn{left:135px;top:433px;width:172px;height:55px;background:var(--teal);color:var(--white);font-family:"Oswald",sans-serif;font-size:20px;display:flex;align-items:center;justify-content:center;gap:12px;letter-spacing:1px}
.slider-arrow{top:608px;width:42px;height:42px;border-radius:50%;background:var(--teal);display:flex;align-items:center;justify-content:center;z-index:2}

/* menu */
.menu{left:0;top:640px;width:1200px;height:543px;background:var(--teal)}
.section-title{width:1200px;left:0;text-align:center;font-size:34px;color:var(--white)}
.section-title::after{content:"";display:block;width:110px;height:3px;background:var(--white);margin:8px auto 0}
.menu-card{top:122px;width:460px;height:343px}
.menu-label{top:432px;height:60px;padding:0 22px;background:var(--teal);border:3px solid var(--white);box-shadow:0 2px 6px rgba(0,0,0,.25);color:var(--white);font-family:"Oswald",sans-serif;font-size:30px;display:flex;align-items:center;transform:translateX(-50%)}

/* about */
.about{left:0;top:1183px;width:1200px;height:367px;background:var(--paper)}
.about-title{left:130px;top:45px;font-size:30px;color:var(--teal)}
.about-title::after{content:"";display:block;width:110px;height:2px;background:var(--teal);margin-top:6px}
.about-copy{left:130px;top:115px;width:430px;font-size:12.5px;line-height:22px;color:var(--muted);text-align:justify}
.about-copy p+p{margin-top:18px}
.about-divider{left:602px;top:55px;width:2px;height:260px;background:#cfcfcf}
.about-photo{left:644px;top:53px;width:421px;height:260px;background:linear-gradient(90deg,#3f4656,#8a8f98 45%,#e8e6e1 70%,#cfcac0);border:6px solid var(--white);box-shadow:4px 6px 10px rgba(0,0,0,.25)}

/* news */
.news{left:0;top:1550px;width:1200px;height:510px;background:linear-gradient(180deg,#2b2623,#3a322c 50%,#2a2420)}
.news-title{left:130px;top:40px;font-size:30px;color:var(--teal)}
.news-title::after{content:"";display:block;width:110px;height:2px;background:var(--teal);margin-top:6px}
.news-all{left:940px;top:43px;width:128px;height:40px;background:var(--teal);color:var(--white);font-family:"Oswald",sans-serif;font-size:15px;display:flex;align-items:center;justify-content:center}
.news-card{top:116px;width:303px;height:337px;border:2px solid var(--white);background:rgba(20,18,16,.82);overflow:hidden}
.news-img{left:0;top:0;width:299px;height:202px}
.news-date{left:18px;top:172px;height:28px;padding:0 12px;background:var(--teal);color:var(--white);font-family:"Oswald",sans-serif;font-size:12px;display:flex;align-items:center}
.news-head{left:20px;top:216px;width:265px;color:var(--white);font-family:"Open Sans",sans-serif;font-weight:700;font-size:12.5px;line-height:17px;text-transform:uppercase}
.news-text{left:20px;width:265px;color:#bbb;font-size:11px;line-height:16px}
.news-more{right:10px;bottom:0;width:86px;height:26px;background:var(--white);color:#222;font-family:"Oswald",sans-serif;font-size:12px;display:flex;align-items:center;justify-content:center}

/* blog */
.blog{left:0;top:2060px;width:1200px;height:603px;background:linear-gradient(180deg,#35b9d4,#2aa9c6)}
.blog-panel{left:260px;top:130px;width:808px;height:407px;background:var(--teal-deep)}
.blog-img{left:130px;top:165px;width:320px;height:332px;background:linear-gradient(160deg,#e8efe8,#98b7c4 40%,#4e6f86 65%,#c6443c 80%,#e6e3d8)}
.blog-date{left:245px;top:40px;height:26px;padding:0 12px;background:var(--teal-dark);color:#d6eef4;font-size:11px;font-style:italic;display:flex;align-items:center}
.blog-copy{left:245px;top:80px;width:520px;color:var(--white);font-size:12.5px;line-height:21.5px}
.blog-more{left:245px;top:350px;width:110px;height:36px;border:2px solid var(--white);color:var(--white);font-family:"Oswald",sans-serif;font-size:13px;display:flex;align-items:center;justify-content:center}

/* widgets */
.widgets{left:0;top:2663px;width:1200px;height:462px;background:#e9e9e9}
.widget{top:35px;height:387px;background:var(--white)}
.signup-title{left:0;width:100%;top:30px;text-align:center;font-family:"Oswald",sans-serif;font-size:29px;color:#888}
.signup-title b{color:var(--teal);font-weight:700}
.signup-title::after{content:"";display:block;width:70px;height:2px;background:var(--teal);margin:4px auto 0}
.signup-copy{left:30px;top:100px;width:238px;text-align:center;font-size:12px;line-height:20px;color:#555}
.field{left:34px;width:230px;height:46px;border:1px solid #ccc;font-size:12px;color:#666;display:flex;align-items:center;gap:10px;padding-left:14px}
.signup-btn{left:34px;top:300px;width:230px;height:52px;background:var(--teal);color:var(--white);font-family:"Oswald",sans-serif;font-size:24px;display:flex;align-items:center;justify-content:center;letter-spacing:1px}
.brand-word{font-family:"Open Sans",sans-serif;font-weight:700;color:#222;font-size:22px;display:flex;align-items:center;gap:8px}
.brand-dot{width:14px;height:14px;background:var(--rating)}
.review-btn{right:14px;top:20px;height:24px;padding:0 10px;background:var(--teal);color:var(--white);font-size:11px;font-weight:600;display:flex;align-items:center}
.review{left:20px;width:250px;height:88px;border:1px solid #ddd;box-shadow:0 1px 3px rgba(0,0,0,.12)}
.review-thumb{left:8px;top:10px;width:70px;height:60px}
.review-text{left:88px;top:10px;width:150px;font-size:11px;line-height:15px;color:#444}
.stars{left:88px;top:60px;display:flex;gap:2px;align-items:center;font-size:9px;color:#888}
.stars i{width:11px;height:11px;background:var(--rating);display:block}
.stars span{margin-left:6px}
.fl-title{left:18px;top:16px;font-family:"Oswald",sans-serif;font-size:14px;color:var(--teal)}
.fl-like{right:16px;top:14px;height:22px;padding:0 8px;background:#4a67a8;color:var(--white);font-size:11px;font-weight:600;display:flex;align-items:center;gap:4px}
.fl-box{left:20px;top:55px;width:263px;height:245px;border:1px solid #ddd}
</style>
</head>
<body>

<!-- Hero -->
<div class="abs hero photo" role="img" aria-label="Plate of grilled steak, roasted potatoes and fresh strawberry"></div>
<div class="abs hero-shade"></div>
<div class="abs logo">RM'S BISTRO</div>
<nav class="abs nav">
  <a class="active">Home</a><a>About Us</a><a>Menu</a><a>Our Coffee</a><a>Gallery</a><a>News</a><a>Contact</a>
</nav>
<div class="abs nav-phone">
  <svg width="12" height="12" viewBox="0 0 24 24"><path fill="#fff" d="M6.6 10.8a15 15 0 0 0 6.6 6.6l2.2-2.2c.3-.3.7-.4 1-.2 1.1.4 2.3.6 3.6.6.6 0 1 .4 1 1V20c0 .6-.4 1-1 1A17 17 0 0 1 3 4c0-.6.4-1 1-1h3.5c.6 0 1 .4 1 1 0 1.3.2 2.5.6 3.6.1.3 0 .7-.2 1z"/></svg>
  (888) 555 0199
</div>
<h1 class="abs heading hero-title">Soups &amp; Salads</h1>
<div class="abs hero-btn">READ MORE
  <svg width="10" height="16" viewBox="0 0 10 16"><path d="M2 2l6 6-6 6" stroke="#fff" stroke-width="2.2" fill="none"/></svg>
</div>
<div class="abs slider-arrow" style="left:548px">
  <svg width="12" height="16" viewBox="0 0 12 16"><path d="M9 2L3 8l6 6" stroke="#fff" stroke-width="2.5" fill="none"/></svg>
</div>
<div class="abs slider-arrow" style="left:612px">
  <svg width="12" height="16" viewBox="0 0 12 16"><path d="M3 2l6 6-6 6" stroke="#fff" stroke-width="2.5" fill="none"/></svg>
</div>

<!-- Our menu -->
<section class="abs menu">
  <h2 class="abs heading section-title" style="top:44px">Our Menu</h2>
  <div class="abs photo menu-card" style="left:130px;background:linear-gradient(160deg,#d8d4cc,#e9c98e 40%,#c88a45 65%,#9c9a96)" role="img" aria-label="Stack of pancakes with butter and a strawberry"></div>
  <div class="abs photo menu-card" style="left:610px;background:linear-gradient(160deg,#e3dfd6,#c48b4c 35%,#6a3a1e 65%,#d6d2c8)" role="img" aria-label="Lunch plate of glazed pastry with braised vegetables"></div>
  <div class="abs menu-label" style="left:360px">BREAKFAST</div>
  <div class="abs menu-label" style="left:840px">LUNCH</div>
</section>

<!-- About -->
<section class="abs about">
  <h2 class="abs heading about-title">About Us</h2>
  <div class="abs about-copy">
    <p>RM's Bistro is committed to superior food quality and cultivating a pleasurable and welcoming dining experience, akin to enjoying a home-cooked meal. We are truly excited to bring a fresh, new restaurant for breakfast and lunch to the City of Champions.</p>
    <p>From the warm welcome our guests will receive as they walk through our doors, through to the last bite of one of our savory dishes, we plan to take the dining experience you'd find in a critically acclaimed restaurant in Boston, and bring to the South Shore.</p>
  </div>
  <div class="abs about-divider"></div>
  <div class="abs photo about-photo" role="img" aria-label="Owner and head chef standing together in the restaurant"></div>
</section>

<!-- News & events -->
<section class="abs news">
  <h2 class="abs heading news-title">News &amp; Events</h2>
  <div class="abs news-all">READ ALL NEWS</div>

  <article class="abs news-card" style="left:130px">
    <div class="abs photo news-img" style="background:linear-gradient(150deg,#cfd2d4,#8f9aa2 50%,#4a4f55)" role="img" aria-label="Chef at work in the kitchen"></div>
    <div class="abs news-date">DECEMBER 16, 2014</div>
    <h3 class="abs news-head">Restaurant offers taste of upper crust in Harlow Bay</h3>
    <p class="abs news-text" style="top:256px">SOURCE: www.harborledger.com (Photo Credit: Dale Morrow/The Ledger) HARLOW BAY...</p>
    <div class="abs news-more">READ MORE</div>
  </article>

  <article class="abs news-card" style="left:447px">
    <div class="abs photo news-img" style="background:linear-gradient(150deg,#a7b08d,#e9e4d8 45%,#c9b49a 75%,#6b5a48)" role="img" aria-label="Plated breakfast with greens"></div>
    <div class="abs news-date">DECEMBER 16, 2014</div>
    <h3 class="abs news-head">Thank you!</h3>
    <p class="abs news-text" style="top:240px">We love Harlow Bay and we thank you! What a great time of year to say thanks.</p>
    <div class="abs news-more">READ MORE</div>
  </article>

  <article class="abs news-card" style="left:765px">
    <div class="abs photo news-img" style="background:linear-gradient(150deg,#8fb6c6,#d8b27a 45%,#a8502f 70%,#6f8a5a)" role="img" aria-label="Sandwich with a glass of lemonade"></div>
    <div class="abs news-date">DECEMBER 16, 2014</div>
    <h3 class="abs news-head">Recipe for lemon-thyme lemonade revealed!</h3>
    <p class="abs news-text" style="top:256px">Remember this picture? We posted this on Photoreel a couple of weeks after our grand...</p>
    <div class="abs news-more">READ MORE</div>
  </article>
</section>

<!-- Latest blog -->
<section class="abs blog">
  <h2 class="abs heading section-title" style="top:50px">Latest Blog</h2>
  <div class="abs blog-panel">
    <div class="abs blog-date">Posted on Feb 22, 2016</div>
    <p class="abs blog-copy">Working in the hospitality business for as long as my father and I have, I sometimes think I can no longer be amazed because we've seen it all, been through a lot and made it out alive somehow. However, since opening up the restaurant we've both thrown aback almost every single day. What makes it, for me, what really weaves it all together is the amazing sense of community we get to experience. Complete strangers sitting adjacent and exchanging great conversation. As simple and trivial as that may sound it's something I definitely don't take for granted. I know for a fact that we have had guests who met for the first time at RM's and are now good friends and I take great joy in knowing that we at least had a tiny part in making that happen. We've connected with some amazing families and have seen their little toddlers grow up before our eyes...and making them smile is so much fun!</p>
    <div class="abs blog-more">READ MORE</div>
  </div>
  <div class="abs photo blog-img" role="img" aria-label="Diner counter with red stools and bright windows"></div>
</section>

<!-- Widgets -->
<section class="abs widgets">
  <div class="abs widget" style="left:130px;width:298px">
    <h3 class="abs signup-title"><b>NEWSLETTER</b> SIGNUP!</h3>
    <p class="abs signup-copy">Subscribe to our mailing list and stay up to date with news, recipes, events + more!</p>
    <div class="abs field" style="top:176px">
      <svg width="12" height="12" viewBox="0 0 24 24"><circle cx="12" cy="8" r="5" fill="#888"/><path d="M3 22c0-5 4-8 9-8s9 3 9 8z" fill="#888"/></svg>Name</div>
    <div class="abs field" style="top:234px">
      <svg width="12" height="12" viewBox="0 0 24 24"><rect x="2" y="5" width="20" height="14" fill="none" stroke="#888" stroke-width="2"/><path d="M2 5l10 8 10-8" fill="none" stroke="#888" stroke-width="2"/></svg>E-mail id</div>
    <div class="abs signup-btn">SIGNUP!</div>
  </div>

  <div class="abs widget" style="left:450px;width:291px">
    <div class="abs brand-word" style="left:20px;top:16px"><span class="brand-dot"></span>Dinetip</div>
    <div class="abs review-btn">Write Review</div>
    <div class="abs review" style="top:72px">
      <div class="abs photo review-thumb" style="background:linear-gradient(135deg,#c9a36c,#6b4a2e)" role="img" aria-label="Reviewer dish photo"></div>
      <p class="abs review-text">Lorem Ipsum is simply dummy text of the printing</p>
      <div class="abs stars"><i></i><i></i><i></i><i></i><i></i><span>20 reviews</span></div>
    </div>
    <div class="abs review" style="top:172px">
      <div class="abs photo review-thumb" style="background:linear-gradient(135deg,#b8b3aa,#5a5550)" role="img" aria-label="Reviewer profile photo"></div>
      <p class="abs review-text">It is a long established fact that a reader will be distracted</p>
      <div class="abs stars"><i></i><i></i><i></i><i></i><i></i><span>20 reviews</span></div>
    </div>
    <div class="abs review" style="top:272px">
      <div class="abs photo review-thumb" style="background:linear-gradient(135deg,#d2b487,#7c5434)" role="img" aria-label="Reviewer dish photo"></div>
      <p class="abs review-text">There are many variations of passages of Lorem Ipsum</p>
      <div class="abs stars"><i></i><i></i><i></i><i></i><i></i><span>20 reviews</span></div>
    </div>
  </div>

  <div class="abs widget" style="left:765px;width:303px">
    <div class="abs fl-title">LIKE US ON FRIENDLOOP</div>
    <div class="abs fl-like">Like</div>
    <div class="abs fl-box">
      <div class="abs photo" style="left:0;top:0;width:261px;height:110px;background:linear-gradient(135deg,#7d8a92,#c8c2b6)" role="img" aria-label="Restaurant page cover photo"></div>
      <div class="abs" style="left:10px;top:22px;width:50px;height:50px;background:var(--teal);border:2px solid #fff"></div>
      <div class="abs" style="left:68px;top:26px;color:#fff;font-weight:700;font-size:14px">RM's Bistro</div>
      <div class="abs" style="left:68px;top:46px;color:#eee;font-size:10px">1,110 likes</div>
      <div class="abs" style="left:10px;top:84px;height:20px;padding:0 8px;background:#f6f7f9;border:1px solid #ccc;font-size:10px;display:flex;align-items:center">Like Page</div>
      <div class="abs" style="left:85px;top:84px;height:20px;padding:0 8px;background:#f6f7f9;border:1px solid #ccc;font-size:10px;display:flex;align-items:center">Share</div>
      <div class="abs" style="left:10px;top:122px;font-size:10px;color:#777">Be the first of your friends to like this</div>
      <div class="abs photo" style="left:10px;top:146px;width:240px;height:60px;background:repeating-linear-gradient(90deg,#9aa3ab 0 26px,#fff 26px 30px)" role="img" aria-label="Row of friend profile pictures"></div>
    </div>
  </div>
</section>

<!-- Footer -->
<footer class="abs" style="left:0;top:3125px;width:1200px;height:425px;background:var(--night)">
  <div class="abs" style="left:130px;top:47px;width:185px;height:135px;background:var(--teal);display:flex;align-items:center;justify-content:center;color:#fff;font-family:'Oswald',sans-serif;font-weight:700;font-size:34px">RM'S BISTRO</div>
  <h4 class="abs heading" style="left:362px;top:45px;color:#fff;font-size:15px">Contact Us</h4>
  <div class="abs" style="left:362px;top:80px;color:#ddd;font-size:11.5px;line-height:24px;display:flex;gap:14px">
    <svg width="18" height="18" viewBox="0 0 24 24" style="margin-top:3px"><circle cx="12" cy="12" r="11" fill="none" stroke="#ddd" stroke-width="1.5"/><path d="M12 5a4 4 0 0 0-4 4c0 3 4 8 4 8s4-5 4-8a4 4 0 0 0-4-4z" fill="#ddd"/></svg>
    <div>RM's Bistro<br>410 N. Harbor St.<br>Harlow Bay, MA 02390</div>
  </div>
  <div class="abs" style="left:362px;top:170px;color:#ddd;font-size:11.5px;display:flex;gap:14px;align-items:center">
    <svg width="18" height="18" viewBox="0 0 24 24"><circle cx="12" cy="12" r="11" fill="none" stroke="#ddd" stroke-width="1.5"/><path d="M8.5 7h2l1 3-1.3 1a7 7 0 0 0 2.8 2.8l1-1.3 3 1v2c0 .6-.4 1-1 1A9 9 0 0 1 7.5 8c0-.6.4-1 1-1z" fill="#ddd"/></svg>
    Tel : 508-555-0142
  </div>
  <div class="abs photo" style="left:552px;top:42px;width:516px;height:241px;background:linear-gradient(135deg,#eeeeea,#e2e4df 50%,#d9dcd6)" role="img" aria-label="Street map showing the restaurant location"></div>
  <div class="abs" style="left:130px;top:215px;width:381px;height:61px;border:2px solid #555;display:flex;align-items:center;padding-left:38px;gap:14px">
    <span class="heading" style="color:#fff;font-size:14px;margin-right:10px">Follow us on:</span>
    <span role="img" aria-label="Social link" style="width:34px;height:34px;border:2px solid #ccc;border-radius:50%"></span>
    <span role="img" aria-label="Social link" style="width:34px;height:34px;border:2px solid #ccc;border-radius:50%"></span>
    <span role="img" aria-label="Social link" style="width:34px;height:34px;border:2px solid #ccc;border-radius:50%"></span>
    <span role="img" aria-label="Social link" style="width:34px;height:34px;border:2px solid #ccc;border-radius:50%"></span>
  </div>
  <div class="abs" style="left:0;top:335px;width:1200px;height:90px;background:var(--night-deep)">
    <div class="abs heading" style="left:130px;top:28px;color:#fff;font-size:12px">Links</div>
    <div class="abs" style="left:130px;top:52px;color:#ddd;font-size:10px;letter-spacing:.3px">HOME &nbsp;| &nbsp;ABOUT US &nbsp;| &nbsp;MENU &nbsp;| &nbsp;OUR COFFEE &nbsp;| &nbsp;GALLERY &nbsp;| &nbsp;NEWS &nbsp;| &nbsp;CONTACT</div>
    <div class="abs" style="left:877px;top:38px;color:#ddd;font-size:10px">Copyrights © 2016 All Rights Reserved</div>
  </div>
</footer>

</body>
</html>
```